Business card design for Summit Wallcrafters required

Our company "Boardline Finishing Harbor Works" needs business cards. Make the business cards be found easily amongst 100 other construction business cards. White background, logo centered and large.

Target Market(s)

Customers or builders who need a drywaller and customers who need a very high quality drywaller.

Industry/Entity Type

Construction

Contact Information for Business Card

The business logo centered and large with "Serving Ridgefield County 15+years" in black Italic, and 2 telephone numbers centered beneath written: Ada / Lou: 403-682-1357, and 403-739-2864 beneath. The business cards will be printed in metal with rounded corners.

Colors
ec1f27

Requirements
Must have
• The selected logo. Must be able to see "DRYWALL" from a distance. Must stick out from other business cards.

```html
<!DOCTYPE html>
<html lang="en">
<head>
<meta charset="utf-8">
<title>Summit Wallcrafters – Business Card</title>
<link rel="stylesheet" href="https://fonts.googleapis.com/css2?family=Quicksand:wght@500;700&display=swap">
<style>
  :root {
    --brand-red: #ec1f27;
    --brand-red-deep: #d71920;
    --ink: #1c1c1c;
    --card-white: #fbfbfb;
    --divider-grey: #8f8f8f;
    --page-bg: #e6e4e1;
  }
  html, body {
    margin: 0;
    padding: 0;
    width: 1200px;
    height: 780px;
    overflow: hidden;
    background: var(--page-bg);
  }
  .canvas {
    position: relative;
    width: 1200px;
    height: 780px;
    display: flex;
    align-items: center;
    justify-content: center;
  }
  .business-card {
    position: relative;
    width: 1000px;
    height: 572px;
    border-radius: 30px;
    background: linear-gradient(135deg, #ffffff 0%, var(--card-white) 55%, #ededed 100%);
    box-shadow: 0 10px 30px rgba(0,0,0,0.18);
    overflow: hidden;
    font-family: "Quicksand", sans-serif;
  }
  .side-band {
    position: absolute;
    left: 0;
    top: 0;
    width: 150px;
    height: 100%;
    background: linear-gradient(90deg, var(--brand-red-deep) 0%, var(--brand-red) 100%);
  }
  .band-divider {
    position: absolute;
    left: 150px;
    top: 0;
    width: 10px;
    height: 100%;
    background: linear-gradient(90deg, #ffffff 0 6px, var(--divider-grey) 6px 8px, transparent 8px);
  }
  .brand-mark {
    position: absolute;
    left: 96px;
    top: 60px;
    width: 110px;
    height: 110px;
    background: var(--brand-red);
    border: 8px solid #ffffff;
    box-shadow: 0 0 0 2px #e2e2e2;
  }
  .brand-name {
    position: absolute;
    left: 236px;
    top: 86px;
    margin: 0;
    width: 720px;
    font-weight: 700;
    font-size: 42px;
    line-height: 1.1;
    white-space: nowrap;
    color: var(--brand-red);
  }
  .service-line {
    position: absolute;
    left: 236px;
    top: 250px;
    margin: 0;
    font-weight: 500;
    font-size: 32px;
    white-space: nowrap;
    color: var(--ink);
  }
  .contact-list {
    position: absolute;
    left: 236px;
    top: 360px;
    margin: 0;
    padding: 0;
    list-style: none;
    font-weight: 500;
    font-size: 28px;
    line-height: 1.5;
    color: var(--ink);
  }
  .contact-name {
    color: var(--brand-red);
  }
</style>
</head>
<body>
  <main class="canvas">
    <section class="business-card" aria-label="Business card front">
      <div class="side-band"></div>
      <div class="band-divider"></div>
      <div class="brand-mark" aria-hidden="true"></div>
      <h1 class="brand-name">Boardline Finishing Harbor Works</h1>
      <p class="service-line">Serving Ridgefield County 15+years</p>
      <ul class="contact-list">
        <li><span class="contact-name">Ada :</span> 403-682-1357</li>
        <li><span class="contact-name">Lou :</span> 403-739-2864</li>
      </ul>
    </section>
  </main>
</body>
</html>
```